Lend a Lantern Website Design (design layout only)

We need a website design for a new nonprofit organization based in Des Moines, Iowa called Lend a Lantern. The nonprofit provides soccer training opportunities to youth soccer players looking to improve their game while also affecting the lives of the less fortunate in a positive way. While participating in the training programs the players also go out and raise money for selected charities. The organization then donates the funds. In its first 18 months we donated $10,500. We would like to see designs attempt to symbolize the mission of the nonprofit - essentially "improve you while improving someone else."

We would like to see the following features:

· A place to donate - Our intent is to have the home page linked to the donation page; a simple straight-forward process for people to give money, and make donating as painless as possible - no account needed to make a donation, credit card or e-check should be the only information needed to donate, and have it be on a single page.

· A photo gallery so people can browse the photo gallery to get a better understanding of our organization and a place to add videos and a calendar to show upcoming events

· A place for contact information and the profiles of directors and board members. This should include a spot showing all the charities the organization donates to. Also includes a news section/blog for comments and suggestions.

We want the design to revolve around the content and mission. We would really like to stress our organization as nonprofit. We would also like if the website was user friendly and easy to navigate.

The logo of our organization is uploaded

```html
<!DOCTYPE html>
<html lang="en">
<head>
<meta charset="utf-8">
<title>Lend a Lantern</title>
<link href="https://fonts.googleapis.com/css2?family=Open+Sans:wght@400;600;700;800&display=swap" rel="stylesheet">
<style>
:root{
  --green:#7ba23f;
  --green-dark:#5f8530;
  --green-band:#6e9839;
  --ink:#333;
  --muted:#888;
  --line:#e2e2e2;
  --topbar:#2d2d2d;
  --footer:#262626;
  --footer-deep:#1b1b1b;
  --pale:#f3f3f3;
  --white:#fff;
}
*{box-sizing:border-box;margin:0;padding:0}
html,body{width:1200px;height:2320px;overflow:hidden}
body{font-family:"Open Sans",Arial,sans-serif;color:var(--ink);background:var(--white);font-size:13px}
.wrap{width:1060px;margin:0 auto;position:relative}
/* top bar */
.topbar{height:32px;background:var(--topbar);color:#bbb;font-size:11px}
.topbar .wrap{display:flex;gap:28px;align-items:center;height:32px}
.topbar span{display:flex;align-items:center;gap:6px}
/* header */
.header{height:80px;border-bottom:1px solid var(--line)}
.header .wrap{display:flex;justify-content:space-between;align-items:center;height:80px}
.brand{display:flex;align-items:center;gap:10px;font-weight:800;font-size:22px;color:var(--green);text-transform:uppercase;letter-spacing:1px;white-space:nowrap}
.brand .mark{width:26px;height:26px;background:var(--green)}
.nav{display:flex;gap:4px}
.nav a{font-size:12px;color:#555;text-decoration:none;padding:10px 14px;font-weight:600}
.nav a.active{background:var(--green);color:#fff}
/* hero */
.hero{height:348px;position:relative;background:linear-gradient(#6da2d6 0%,#a9cbe9 55%,#7aa54a 70%,#4f7d2c 100%)}
.hero-photo{position:absolute;right:90px;top:0;width:380px;height:348px;background:radial-gradient(ellipse at 50% 55%,#2f4f8a 0%,#3f5f9a 35%,rgba(63,95,154,0) 70%)}
.hero-copy{position:absolute;left:70px;top:70px;width:560px;color:#fff}
.hero-copy h1{font-size:44px;font-weight:700;display:flex;align-items:center;gap:14px;white-space:nowrap}
.hero-copy h1 .brand{background:#fff;padding:6px 12px;font-size:22px}
.hero-copy p{font-size:13px;line-height:1.6;margin:18px 0 26px;width:500px}
.btn{display:inline-block;background:var(--green);color:#fff;font-weight:600;font-size:12px;padding:10px 20px;border-radius:3px}
/* involved */
.involved{height:380px;background:var(--green-band);color:#fff;padding-top:38px}
.involved h2{font-size:22px;font-weight:700}
.involved h2 + .rule{width:60px;height:3px;background:#fff;margin:10px 0 30px}
.row{display:flex;gap:26px;margin-bottom:26px}
.field{flex:1}
.field label{display:block;font-size:12px;margin-bottom:8px}
.input{height:36px;background:#fff;border-radius:2px;position:relative}
.input.select:after{content:"";position:absolute;right:0;top:0;width:32px;height:36px;background:#e6e6e6}
.radios{display:flex;gap:26px;height:36px;align-items:center;font-size:12px}
.radios span{display:flex;align-items:center;gap:8px}
.radios i{width:14px;height:14px;border-radius:50%;background:#fff;display:inline-block}
.radios i.on{box-shadow:inset 0 0 0 4px #fff;background:var(--green-dark)}
.btn-light{background:#fff;color:var(--green-dark);font-weight:700;font-size:13px;padding:11px 22px;border-radius:3px;display:inline-flex;gap:8px;align-items:center}
/* news & causes */
.split{height:330px;padding-top:48px}
.split .wrap{display:flex;gap:50px}
.col-head{display:flex;justify-content:space-between;align-items:center;border-bottom:1px solid var(--line);padding-bottom:10px;margin-bottom:22px}
.col-head h3{font-size:18px;font-weight:700}
.col-head h3 span{font-weight:400}
.arrows{color:#aaa;font-size:14px;letter-spacing:6px}
.news{width:430px}
.news-item{display:flex;gap:20px}
.news-item h4{font-size:13px;margin-bottom:10px}
.news-item p{font-size:11px;color:var(--muted);line-height:1.6}
.news-photo{width:190px;height:150px;flex:none;background:linear-gradient(135deg,#6f9a4a,#c9d7b6 60%,#4a6f2f)}
.causes{flex:1}
.cause-grid{display:grid;grid-template-columns:1fr 1fr;gap:26px 30px}
.cause{display:flex;gap:16px}
.cause .ic{width:54px;height:54px;border-radius:50%;border:2px solid #ccc;flex:none;display:flex;align-items:center;justify-content:center}
.cause h5{font-size:14px;font-weight:600;margin:6px 0 6px}
.cause p{font-size:11px;color:var(--muted);line-height:1.5}
/* testimonial */
.quote{height:270px;background:var(--pale);text-align:center;padding-top:24px}
.quote .avatar{width:86px;height:86px;margin:0 auto;border:4px solid #fff;background:linear-gradient(#d9c7b2,#a38668)}
.quote p{width:860px;margin:18px auto 0;font-size:12px;color:#666;line-height:1.7}
.quote h6{font-size:17px;font-weight:700;margin-top:14px}
.dots{display:flex;justify-content:center;gap:8px;margin-top:12px}
.dots i{width:12px;height:12px;border-radius:50%;border:2px solid #999}
.dots i.on{background:#666;border-color:#666}
/* gallery */
.gallery{height:380px;padding-top:40px}
.strip{display:flex;margin-top:6px;height:250px}
.shot{flex:1}
.shot.a{background:linear-gradient(#e6ebef,#5c8a3b)}
.shot.b{background:linear-gradient(#86a862,#3e6a2a)}
.shot.c{background:linear-gradient(#9eb9c8,#3b6c9c 60%,#5e8a3a);position:relative}
.shot.d{background:linear-gradient(#c7d3dc,#4f7f31)}
.shot.e{background:linear-gradient(#dfe6dc,#7b3030 50%,#4d7b2f)}
.caption{position:absolute;left:0;right:0;bottom:0;background:rgba(0,0,0,.75);color:#fff;text-align:center;padding:14px}
.caption strong{display:block;font-size:13px}
.caption span{font-size:11px;color:#ccc}
/* footer */
.footer{height:450px;background:var(--footer);color:#bbb;padding-top:50px}
.footer .wrap{display:flex;gap:40px}
.fcol{width:200px}
.fcol h4{color:#fff;font-size:14px;font-weight:700;margin-bottom:20px;text-transform:uppercase}
.fcol h4 b{color:var(--green)}
.fcol p{font-size:11px;line-height:1.7}
.thumbs{display:grid;grid-template-columns:repeat(3,56px);gap:8px}
.thumbs i{height:56px;background:linear-gradient(135deg,#6b7f58,#3c4a34)}
.contact-line{display:flex;gap:10px;font-size:11px;margin-bottom:14px;line-height:1.5}
.contact-line svg{flex:none;margin-top:2px}
.newsletter{width:290px;background:var(--green);padding:22px;color:#fff;margin-left:auto;margin-top:-50px;height:300px}
.newsletter h4{font-size:14px;font-weight:700;margin-bottom:14px}
.newsletter p{font-size:11px;line-height:1.6;margin-bottom:18px}
.newsletter .input{height:32px;margin-bottom:16px}
.social{display:flex;gap:8px;margin-bottom:16px}
.social i{width:26px;height:26px;background:var(--green-dark)}
.btn-dark{display:inline-block;background:var(--footer);color:#fff;font-size:11px;padding:8px 16px}
.bottom{height:50px;background:var(--footer-deep);color:#888;font-size:11px}
.bottom .wrap{display:flex;justify-content:space-between;align-items:center;height:50px}
.bottom nav{display:flex;gap:20px}
</style>
</head>
<body>
<div class="topbar"><div class="wrap">
  <span><svg width="10" height="12" viewBox="0 0 10 12"><path d="M5 0a4 4 0 0 1 4 4c0 3-4 8-4 8S1 7 1 4a4 4 0 0 1 4-4z" fill="#7ba23f"/></svg>418 Elm Court Walk, Des Moines</span>
  <span><svg width="11" height="11" viewBox="0 0 11 11"><path d="M2 0l2 3-1 1.5a7 7 0 0 0 3.5 3.5L8 7l3 2-1 2C5 11 0 6 0 1z" fill="#7ba23f"/></svg>(515) 555-0142</span>
  <span><svg width="12" height="9" viewBox="0 0 12 9"><rect width="12" height="9" fill="#7ba23f"/><path d="M0 0l6 5 6-5" stroke="#2d2d2d" fill="none"/></svg>hello@lendalantern.org</span>
</div></div>

<header class="header"><div class="wrap">
  <div class="brand"><i class="mark"></i>Lend a Lantern</div>
  <nav class="nav">
    <a class="active">Home</a><a>About Us</a><a>Teams</a><a>Get Involved</a><a>Endorsements</a><a>News</a><a>Contact Us</a>
  </nav>
</div></header>

<section class="hero">
  <div class="hero-photo" role="img" aria-label="Young player in a blue kit holding a soccer ball on a grass field"></div>
  <div class="hero-copy">
    <h1>Welcome To <span class="brand">Lend a Lantern</span></h1>
    <p>Young players sharpen their game on the field while raising funds for local charities. Every session, every goal and every mile helps someone else in our community grow stronger too.</p>
    <span class="btn">Learn More</span>
  </div>
</section>

<section class="involved"><div class="wrap">
  <h2>Get Involved</h2><div class="rule"></div>
  <div class="row">
    <div class="field"><label>Name*</label><div class="input"></div></div>
    <div class="field"><label>Email*</label><div class="input"></div></div>
    <div class="field"><label>City Number*</label><div class="input"></div></div>
    <div class="field"><label>Donation amount*</label><div class="input select"></div></div>
  </div>
  <div class="row">
    <div class="field" style="flex:2"><label>Select Your Payment Type*</label>
      <div class="radios"><span><i class="on"></i>Credit</span><span><i></i>Debit</span><span><i></i>Prepaid</span><span><i></i>E-Check</span></div></div>
    <div class="field"><label>Credit Card Number*</label><div class="input"></div></div>
    <div class="field"><label>Expiry Date*</label><div class="input select"></div></div>
  </div>
  <span class="btn-light"><svg width="14" height="12" viewBox="0 0 14 12"><path d="M7 12S0 7.5 0 3.5A3.5 3.5 0 0 1 7 2a3.5 3.5 0 0 1 7 1.5C14 7.5 7 12 7 12z" fill="#5f8530"/></svg>Donate Now</span>
</div></section>

<section class="split"><div class="wrap">
  <div class="news">
    <div class="col-head"><h3>Recent <span>News</span></h3><span class="arrows">‹ ›</span></div>
    <div class="news-item">
      <div><h4>Lorem Ipsum Dolor Sit Amet</h4>
      <p>Our spring camp wrapped up with forty players and a bake sale that raised funds for the county food bank. Thank you to every family who helped.<br><br>Next month the teams visit the children's shelter to share a training day.</p></div>
      <div class="news-photo" role="img" aria-label="Youth player celebrating with a soccer ball"></div>
    </div>
  </div>
  <div class="causes">
    <div class="col-head"><h3>Our <span>Causes</span></h3><span class="arrows">‹ ›</span></div>
    <div class="cause-grid">
      <div class="cause"><span class="ic"><svg width="26" height="26" viewBox="0 0 26 26"><circle cx="13" cy="13" r="11" fill="none" stroke="#777" stroke-width="2"/><path d="M13 8l4 3-1.5 5h-5L9 11z" fill="#777"/></svg></span><div><h5>Soccer Gear</h5><p>Boots, balls and kits for kids who need them.</p></div></div>
      <div class="cause"><span class="ic"><svg width="26" height="26" viewBox="0 0 26 26"><circle cx="13" cy="13" r="11" fill="none" stroke="#777" stroke-width="2"/><path d="M2 13h22M13 2v22" stroke="#777" stroke-width="2"/></svg></span><div><h5>Football Leagues</h5><p>Fees covered so every child can join a team.</p></div></div>
      <div class="cause"><span class="ic"><svg width="26" height="26" viewBox="0 0 26 26"><path d="M13 22S3 15.5 3 9a5 5 0 0 1 10-1 5 5 0 0 1 10 1c0 6.5-10 13-10 13z" fill="none" stroke="#777" stroke-width="2"/></svg></span><div><h5>Charity Matches</h5><p>Friendly games that raise money for partners.</p></div></div>
      <div class="cause"><span class="ic"><svg width="26" height="26" viewBox="0 0 26 26"><rect x="3" y="6" width="20" height="15" rx="2" fill="none" stroke="#777" stroke-width="2"/><path d="M13 9v9M8.5 13.5h9" stroke="#777" stroke-width="2"/></svg></span><div><h5>First Aid</h5><p>Training and kits for clubs across the city.</p></div></div>
    </div>
  </div>
</div></section>

<section class="quote">
  <div class="avatar" role="img" aria-label="Portrait of the organization's CEO"></div>
  <p>“Watching our players grow on the field while they lift up neighbours off it is the reason we started. Every hour of practice turns into something bigger than a game, and every dollar raised goes straight to a family or a cause that needs it. Thank you for standing with us and helping us light the way for others.”</p>
  <h6>M.R. Whitfield, CEO</h6>
  <div class="dots"><i></i><i class="on"></i><i></i></div>
</section>

<section class="gallery"><div class="wrap">
  <div class="col-head"><h3>Photo <span>Gallery</span></h3><span class="arrows">‹ ›</span></div>
</div>
  <div class="strip">
    <div class="shot a" role="img" aria-label="Soccer ball resting on grass"></div>
    <div class="shot b" role="img" aria-label="Youth team posing on the field"></div>
    <div class="shot c" role="img" aria-label="Player in blue chasing the ball"><div class="caption"><strong>LOREM IPSUM DOLOR SIT</strong><span>Amet adipiscing consectetuer</span></div></div>
    <div class="shot d" role="img" aria-label="Two players contesting the ball in a match"></div>
    <div class="shot e" role="img" aria-label="Players in red kits during a game"></div>
  </div>
</section>

<footer class="footer"><div class="wrap">
  <div class="fcol"><h4><b>People</b> Reviews</h4>
    <p>“Our son found confidence, friends and a reason to give back. The coaches care about the player and the person, and it shows in every session.”<br><br>— A proud parent</p></div>
  <div class="fcol"><h4><b>Snapshot</b> Feed</h4>
    <div class="thumbs" role="img" aria-label="Grid of small photos from recent events"><i></i><i></i><i></i><i></i><i></i><i></i><i></i><i></i><i></i></div></div>
  <div class="fcol"><h4><b>Contact</b> Us</h4>
    <div class="contact-line"><svg width="10" height="12" viewBox="0 0 10 12"><path d="M5 0a4 4 0 0 1 4 4c0 3-4 8-4 8S1 7 1 4a4 4 0 0 1 4-4z" fill="#7ba23f"/></svg><span>418 Elm Court Walk<br>Des Moines, IA 50309</span></div>
    <div class="contact-line"><svg width="11" height="11" viewBox="0 0 11 11"><path d="M2 0l2 3-1 1.5a7 7 0 0 0 3.5 3.5L8 7l3 2-1 2C5 11 0 6 0 1z" fill="#7ba23f"/></svg><span>(515) 555-0142<br>(515) 555-0187</span></div>
    <div class="contact-line"><svg width="12" height="9" viewBox="0 0 12 9"><rect width="12" height="9" fill="#7ba23f"/><path d="M0 0l6 5 6-5" stroke="#262626" fill="none"/></svg><span>hello@lendalantern.org</span></div>
  </div>
  <div class="newsletter"><h4>SIGNUP NEWSLETTER</h4>
    <p>Get news on camps, matches and the causes we support.</p>
    <div class="input"></div>
    <div class="social"><i></i><i></i><i></i><i></i><i></i></div>
    <span class="btn-dark">Submit</span></div>
</div></footer>

<div class="bottom"><div class="wrap">
  <span>Copyright © All rights reserved</span>
  <nav><span>Home</span><span>About Us</span><span>Teams</span><span>Get Involved</span><span>Endorsements</span><span>News</span><span>Contact Us</span></nav>
</div></div>
</body>
</html>
```